Business Card Design Project - Tall Maple

We are looking for a new business card design. Our company name is Tall Maple Communication Solutions. Our primary function is to provide our clients with communication solutions. These solutions include commercial phone systems and T1 and Fiber Internet lines. Another major part of the business is cabling new buildings with CAT5 cable for both data and phone.

Industry/Entity Type

Communication

Requirements
Must have
• The cards need to be two sided and have some bleeding edge color.
Nice to have
• We are going to upload our current logo BUT we are not married to this logo. If you want to incorporate a re-designed logo with the new business card - please feel free to do so. We are looking for a new bold look that is very colorful yet professional.

```html
<!DOCTYPE html>
<html lang="en">
<head>
<meta charset="utf-8">
<title>Tall Maple Communication Solutions – Business Card</title>
<link href="https://fonts.googleapis.com/css2?family=Quicksand:wght@400;500&display=swap" rel="stylesheet">
<style>
  :root {
    --bg-left: #e9e9e9;
    --bg-right: #ffffff;
    --card-front: #c3e7f4;
    --card-back-light: #e8f6fc;
    --brand-blue: #1fa6d8;
    --label-blue: #3fb1dc;
    --soft-blue: #a9d9ec;
    --dot-blue: #8fd0ea;
  }
  * { margin: 0; padding: 0; box-sizing: border-box; }
  html, body { width: 1200px; height: 1200px; overflow: hidden; }
  body {
    position: relative;
    background: linear-gradient(90deg, var(--bg-left) 0%, #f7f7f7 55%, var(--bg-right) 100%);
    font-family: "Quicksand", sans-serif;
  }
  .card { position: absolute; border-radius: 30px; overflow: hidden; }
  .card-front {
    left: 38px; top: 443px; width: 548px; height: 312px;
    background: var(--card-front);
  }
  .card-back { left: 610px; top: 442px; width: 556px; height: 316px; }
  .card-back .backdrop { position: absolute; inset: 0; width: 100%; height: 100%; }

  .brand { position: absolute; text-align: center; color: var(--brand-blue); }
  .brand .name { font-weight: 400; text-transform: uppercase; line-height: 1; white-space: nowrap; }
  .brand .tagline { font-weight: 400; text-transform: uppercase; line-height: 1; white-space: nowrap; }

  .card-front .brand { left: 0; right: 0; top: 177px; }
  .card-front .brand .name { font-size: 40px; letter-spacing: 1.5px; }
  .card-front .brand .tagline { font-size: 17px; letter-spacing: 1.6px; margin-top: 7px; }

  .card-back .brand { left: 40px; width: 176px; top: 180px; }
  .card-back .brand .name { font-size: 24px; letter-spacing: .4px; }
  .card-back .brand .tagline { font-size: 10px; letter-spacing: .3px; margin-top: 3px; }

  .contact { position: absolute; right: 54px; top: 44px; text-align: right; line-height: 1; }
  .contact .person { font-size: 30px; color: var(--brand-blue); letter-spacing: 1px; font-weight: 400; }
  .contact .address { margin-top: 10px; font-size: 17px; color: var(--soft-blue); }
  .contact .address p { margin-bottom: 8px; }
  .contact .divider { display: flex; justify-content: flex-end; gap: 31px; margin: 12px 0 16px; }
  .contact .divider span { width: 5px; height: 5px; border-radius: 50%; background: var(--dot-blue); }
  .contact .divider span:nth-child(1) { opacity: .35; }
  .contact .divider span:nth-child(2) { opacity: .5; }
  .contact .divider span:nth-child(3) { opacity: .7; }
  .contact .divider span:nth-child(4) { opacity: .85; }
  .contact .divider span:nth-child(5) { background: var(--brand-blue); }
  .contact .lines { font-size: 17px; }
  .contact .lines p { margin-bottom: 9px; }
  .contact .label { color: var(--label-blue); }
  .contact .value { color: var(--soft-blue); }
</style>
</head>
<body>

  <section class="card card-front">
    <div class="brand">
      <div class="name">Tall Maple</div>
      <div class="tagline">Communication Solutions</div>
    </div>
  </section>

  <section class="card card-back">
    <svg class="backdrop" viewBox="0 0 556 316" preserveAspectRatio="none">
      <rect width="556" height="316" fill="var(--card-back-light)"/>
      <path d="M0 0 H192 C270 60 300 200 200 316 H0 Z" fill="var(--card-front)"/>
    </svg>
    <div class="brand">
      <div class="name">Tall Maple</div>
      <div class="tagline">Communication Solutions</div>
    </div>
    <div class="contact">
      <div class="person">Devin Marlowe</div>
      <div class="address">
        <p>1840 N. Larkspur Ave</p>
        <p>Ste. 410</p>
        <p>Tucson, AZ 85719</p>
      </div>
      <div class="divider"><span></span><span></span><span></span><span></span><span></span></div>
      <div class="lines">
        <p><span class="label">Office:</span> <span class="value">520.555.0148</span></p>
        <p><span class="label">Cell:</span> <span class="value">520.555.0172</span></p>
        <p><span class="label">24/7:</span> <span class="value">800.555.0136</span></p>
        <p><span class="label">Fax:</span> <span class="value">800.555.0191</span></p>
      </div>
    </div>
  </section>

</body>
</html>
```